Company truck wrap design

We are The Drain Mending Works - We are looking to have the car wrapped, and need the expertise of a GD.

Below is the logo and photos of the truck.
1. We require an image to be created that offers a before and after of what we do - a story at a glance in essence

2. These images MUST be clean and pop! NO BACKGROUND effects - eg see images attached - we do not want any background imagery simply the pipe.

3. The image attached displays in essence what we require...
Tree roots, broken pipe and then a pipe that has been fixed with our resign (note the green) However,  In place of the green we would like our logo "the swirl" to be placed in the crack of the pipe replacing the single colour green .  We believe this will show exactly what we do in a simple and non verbal way.

4. We would like the images to run along of the upper sides of the canopy - as big as possible but not overpowering in size.

5. The back of the canopy could potentially have the pipe running around the top also. We require the logo contact number and website to be included on all sides

6. The dual cab two doors each side - The doors to display the logo, phone number and the website.

We are open to any suggestions - however - we like clean lines, bold but not overwhelming.

It would  be good to include
(dot points) - the dot could be our logo!
blocked drains
CCTV Inspections
Pipe Relining
Pipe Coating

I have included the brand guide
We are moving on this quickly

The Car is a 2020 VOLKAN TRAVERSO DUAL CAB

We look forward to receiving your work!

Smiles
Marjorie

Target Market(s)

Domestic and Commercial buildings

Requirements
Must have
• logo
phone number
website

```html
<!DOCTYPE html>
<html lang="en">
<head>
<meta charset="utf-8">
<title>The Drain Mending Works – Vehicle Wrap</title>
<link href="https://fonts.googleapis.com/css2?family=Saira+Semi+Condensed:wght@300;400&display=swap" rel="stylesheet">
<style>
  :root {
    --teal: #5cc3be;
    --charcoal: #3a3b3d;
    --charcoal-dark: #2e2f31;
    --swoosh: #4d5052;
    --white: #ffffff;
    --pipe-brown: #b0784a;
    --page: #ffffff;
  }
  html, body {
    margin: 0;
    padding: 0;
    width: 1200px;
    height: 721px;
    overflow: hidden;
    background: var(--page);
  }
  .wrap-sheet {
    display: block;
    width: 1200px;
    height: 721px;
    font-family: "Saira Semi Condensed", sans-serif;
  }
  .body-panel { fill: var(--charcoal); }
  .nose-panel { fill: var(--teal); }
  .swoosh { fill: none; stroke: var(--swoosh); stroke-width: 26; }
  .canopy-panel { fill: var(--charcoal-dark); }
  .brand-dot { fill: var(--teal); }
  .brand-name { fill: var(--white); font-weight: 300; font-size: 21px; letter-spacing: 0.3px; }
  .brand-rule { stroke: var(--white); stroke-width: 0.6; opacity: 0.7; }
  .brand-tag { fill: var(--white); font-weight: 400; font-size: 7.5px; letter-spacing: 0.3px; }
  .door-contact { fill: var(--teal); font-weight: 400; font-size: 13px; letter-spacing: 0.3px; }
  .service { fill: var(--teal); font-weight: 400; font-size: 15px; letter-spacing: 0.3px; }
  .service-dot { fill: none; stroke: var(--teal); stroke-width: 2.6; }
  .rear-canopy { fill: var(--teal); }
  .rear-brand { fill: var(--white); font-weight: 300; font-size: 13.5px; }
  .rear-tag { fill: var(--white); font-size: 5px; }
  .contact-tag { fill: var(--teal); }
  .contact-text { fill: var(--white); font-weight: 400; font-size: 17px; letter-spacing: 0.4px; }
  .stage-label { fill: var(--white); font-size: 11px; }
  .stage-frame { fill: var(--teal); }
</style>
</head>
<body>
<svg class="wrap-sheet" viewBox="0 0 1200 721" xmlns="http://www.w3.org/2000/svg">
  <defs>
    <clipPath id="side-clip">
      <rect x="10" y="135" width="695" height="170" rx="10"/>
    </clipPath>
    <g id="side-panel">
      <rect class="body-panel" x="10" y="135" width="695" height="170" rx="10"/>
      <g clip-path="url(#side-clip)">
        <path class="nose-panel" d="M0 135 L200 135 Q236 200 222 305 L0 305 Z"/>
        <path class="swoosh" d="M478 320 Q495 200 595 185 Q660 180 700 215"/>
        <path class="swoosh" d="M615 182 Q660 235 662 320" opacity="0.7"/>
      </g>
      <rect class="canopy-panel" x="482" y="50" width="210" height="85"/>
    </g>
  </defs>

  <!-- Passenger side -->
  <g class="wrap-side side-right">
    <use href="#side-panel"/>
    <circle class="brand-dot" cx="270" cy="215" r="44"/>
    <text class="brand-name" x="343" y="186">THE DRAIN</text>
    <text class="brand-name" x="343" y="207">MENDING</text>
    <text class="brand-name" x="343" y="228">WORKS</text>
    <line class="brand-rule" x1="343" y1="235" x2="432" y2="235"/>
    <text class="brand-tag" x="343" y="246">NO DIG PIPE REPAIRS</text>
    <text class="door-contact" x="343" y="266">+61 7 5550 1427</text>
    <text class="door-contact" x="343" y="282">thedmw.com.au</text>
    <g class="service-list">
      <circle class="service-dot" cx="533" cy="70" r="4.6"/>
      <text class="service" x="543" y="75">Blocked drains</text>
      <circle class="service-dot" cx="533" cy="85" r="4.6"/>
      <text class="service" x="543" y="90">CCTV Inspections</text>
      <circle class="service-dot" cx="533" cy="100" r="4.6"/>
      <text class="service" x="543" y="105">Pipe Relining</text>
      <circle class="service-dot" cx="533" cy="115" r="4.6"/>
      <text class="service" x="543" y="120">Pipe Coating</text>
    </g>
  </g>

  <!-- Driver side -->
  <g class="wrap-side side-left">
    <use href="#side-panel" transform="translate(737 360) scale(-1 1)"/>
    <circle class="brand-dot" cx="467" cy="575" r="44"/>
    <text class="brand-name" x="302" y="546">THE DRAIN</text>
    <text class="brand-name" x="302" y="567">MENDING</text>
    <text class="brand-name" x="302" y="588">WORKS</text>
    <line class="brand-rule" x1="302" y1="595" x2="391" y2="595"/>
    <text class="brand-tag" x="302" y="606">NO DIG PIPE REPAIRS</text>
    <text class="door-contact" x="302" y="626">+61 7 5550 1427</text>
    <text class="door-contact" x="302" y="642">thedmw.com.au</text>
    <g class="service-list" text-anchor="end">
      <text class="service" x="194" y="435">Blocked drains</text>
      <circle class="service-dot" cx="204" cy="430" r="4.6"/>
      <text class="service" x="194" y="450">CCTV Inspections</text>
      <circle class="service-dot" cx="204" cy="445" r="4.6"/>
      <text class="service" x="194" y="465">Pipe Relining</text>
      <circle class="service-dot" cx="204" cy="460" r="4.6"/>
      <text class="service" x="194" y="480">Pipe Coating</text>
      <circle class="service-dot" cx="204" cy="475" r="4.6"/>
    </g>
  </g>

  <!-- Rear canopy -->
  <g class="wrap-rear">
    <path class="rear-canopy" d="M762 222 L1163 219 L1170 330 L1170 435 L755 435 L755 330 Z"/>
    <rect class="canopy-panel" x="804" y="230" width="321" height="199"/>
    <circle class="brand-dot" cx="857" cy="279" r="30"/>
    <text class="rear-brand" x="894" y="266">THE DRAIN</text>
    <text class="rear-brand" x="894" y="280">MENDING</text>
    <text class="rear-brand" x="894" y="294">WORKS</text>
    <text class="rear-tag" x="894" y="305">NO DIG PIPE REPAIRS</text>
    <path class="contact-tag" d="M983 252 L1121 252 L1121 301 L983 301 L971 276.5 Z"/>
    <text class="contact-text" x="1046" y="274" text-anchor="middle">+61 7 5550 1427</text>
    <text class="contact-text" x="1046" y="293" text-anchor="middle">thedmw.com.au</text>
    <text class="stage-label" x="870" y="330">Before</text>
    <text class="stage-label" x="1017" y="330">After</text>
    <rect class="stage-frame" x="825" y="336" width="133" height="76" rx="5"/>
    <rect x="828" y="345" width="127" height="32" fill="var(--pipe-brown)" role="img" aria-label="Illustration of a cracked clay pipe with tree roots growing through it"/>
    <rect class="stage-frame" x="967" y="336" width="133" height="76" rx="5"/>
    <rect x="970" y="345" width="127" height="32" fill="var(--pipe-brown)" role="img" aria-label="Illustration of the same pipe repaired with a resin lining, roots removed"/>
  </g>
</svg>
</body>
</html>
```